IT Company Business Card Design w/Stationary Design

We have a great logo we like! We are looking to redesign our business cards and all company logo'd merchandise/materials.

We are an IT Company located near the Bay Area (San Francisco, CA). We specialize in Managed Services and offer complete IT Computer and Network Support to Businesses of all sizes. We thrive on making a lasting impression. We have been doing IT for 15yrs+ but are young at heart. We like to stand out and be different. We want to be unique and have a recognizable brand. We need our logo to represent who we are. We are young, professional, creative and outstanding. We don't want to blend in, we want to stand out. Our business card needs to stand out and grab attention. Something Bold, yet simple and clean. (I will provide ideas of what we like to give a taste of what we are looking for).

The design can include any kind of texture/artistic design or sizing EXCEPT please "no square card designs" as they don't seem to fit in wallets very well. We dont mind curved edges, rounded corners, vertical layouts or horizontal layouts, embossing, letter press or raised surfaces. Again, we dont want to look average or plain or boring. :) Be creative - yet practical! We have ordered from Pebblecraft designs before and been very happy. Their card sizes tend to be a little different, so beware. Hope this helps!

Target Market(s)

Businesses - Small to Medium, Corporations, Publicly Traded Companies

Industry/Entity Type

Business

Contact Information for Business Card

Harbor Lantern IT
7318 Quillby Avenue
Suite F
Modesto, CA 95871

Office 209.555.0137
Direct 209.555.0182
Cell 209.555.0164

Ross Tavener
Founder, CEO
www.hlit-example.com
rtavener@hlit-example.com

Locations Serviced: Modesto, Stockton, Pleasanton, Fresno (incorporate this on the card ONLY if there's a good place to do so).

What we specialize in: Computer, Network, Voice, Data. (IT Services)

Our Logo Colors: Black and Blue (#006699). Open to using grey or orange as well - but not required. Don't want too busy....

Logo Font: "Cinthe" (Will attach logo font). We want type style to be clean. You can show different font types including our logo font - and we are open to other font ideas.

The logo can be separated. You can use elements together or apart. Surprise us! :) We "REALLY" want the "hl" to be our identifier/our brand people recognize.

Font styles to use
Sans Serif

Colors
0355a3
3176b5
f37122
f78f20
faa54b
474747
aaaaaa
757575
000000

Requirements
Must have
• Bold, Big, Colorful, Modern/yet Fun, Clean Design, Stand Out Presence, Texture would be welcomed - but not necessary, Card design shape can include cut corners or rounded or square edges. Be creative. (HOWEVER, we don't want a square design because we have found it doesn't fit in wallets that easily).
• We do like using Pebblecraft printing company (Which they have particular sizing on their card templates - beware), but are open to other design templates/printing companies as well. We just want to make sure its easy to find a print company to do our work. Too unique could be costly and hard to get cards printed.
• Colors to use: Our logo Blue (#006699), with either whites, grays, black, shades of our blue, and maybe a pinch of orange if needed. Primarily, blue, white, gray or black.
Nice to have
• Texture would be cool or little different edging or shape - but nothing too costly to print. I have seen cards with 3 sharp edges and one round edge. Something like that would be cool as an option. Or a vertical card.
• I love a faded watermark look. It would be nice to see some shading of our circle logo on a few designs. The circle with "hl" in it OR.... taking just the "hl" and using it alone.
Should not have
• No square card designs. Nothing too expensive or elaborate to print. No busy fonts. Do not like Times New Roman type fonts (too old looking). Not a lot of orange (if you even choose to use some orange).

```html
<!DOCTYPE html>
<html lang="en">
<head>
<meta charset="utf-8">
<title>Harbor Lantern IT – Business Card</title>
<link href="https://fonts.googleapis.com/css2?family=Oxanium:wght@500;600&family=Questrial&display=swap" rel="stylesheet">
<style>
  :root {
    --brand-blue: #2383c0;
    --paper: #fdfdfd;
    --ink: #3a3a3a;
    --muted: #7a7a7a;
    --backdrop: #c3c3c3;
    --white: #ffffff;
  }
  html, body {
    margin: 0;
    padding: 0;
    width: 1200px;
    height: 907px;
    overflow: hidden;
    background: var(--backdrop);
  }
  .canvas {
    position: relative;
    width: 1200px;
    height: 907px;
  }
  .card {
    position: absolute;
    left: 300px;
    width: 600px;
    height: 344px;
    box-sizing: border-box;
    overflow: hidden;
  }
  .card-front {
    top: 92px;
    background: var(--paper);
    border-radius: 22px 0 22px 0;
  }
  .card-back {
    top: 471px;
    background: var(--brand-blue);
    border-radius: 0 22px 22px 22px;
  }
  .person-name {
    position: absolute;
    left: 42px;
    top: 38px;
    margin: 0;
    font: 600 20px/1 "Oxanium", sans-serif;
    letter-spacing: 1.5px;
    color: var(--brand-blue);
  }
  .person-title {
    position: absolute;
    left: 42px;
    top: 70px;
    margin: 0;
    font: 500 15px/1 "Oxanium", sans-serif;
    letter-spacing: 1.5px;
    color: var(--muted);
  }
  .address {
    position: absolute;
    left: 42px;
    top: 112px;
    margin: 0;
    font: 15px/24px "Questrial", sans-serif;
    color: var(--ink);
    font-style: normal;
  }
  .contact-list {
    position: absolute;
    left: 42px;
    top: 193px;
    margin: 0;
    padding: 0;
    list-style: none;
    font: 15px/24px "Questrial", sans-serif;
    color: var(--ink);
  }
  .contact-list li {
    display: flex;
    align-items: center;
    gap: 7px;
  }
  .contact-icon {
    width: 14px;
    height: 14px;
    fill: var(--brand-blue);
    flex: none;
  }
  .brand-block {
    position: absolute;
    right: 44px;
    top: 134px;
    display: flex;
    flex-direction: column;
    align-items: center;
    gap: 16px;
  }
  .brand-dot {
    width: 92px;
    height: 92px;
    border-radius: 50%;
    background: var(--brand-blue);
  }
  .brand-name {
    margin: 0;
    font: 600 27px/1 "Oxanium", sans-serif;
    letter-spacing: 1px;
    color: var(--brand-blue);
  }
  .card-back .brand-name {
    position: absolute;
    left: 35px;
    top: 32px;
    font-size: 31px;
    color: var(--white);
  }
  .brand-dot-large {
    position: absolute;
    right: 22px;
    bottom: 18px;
    width: 300px;
    height: 300px;
    border-radius: 50%;
    background: var(--white);
  }
</style>
</head>
<body>
<main class="canvas">
  <section class="card card-front" aria-label="Card front">
    <h1 class="person-name">Ross Tavener</h1>
    <p class="person-title">Founder, CEO</p>
    <address class="address">
      Harbor Lantern IT<br>
      7318 Quillby Avenue<br>
      Suite F Modesto, CA 95871
    </address>
    <ul class="contact-list">
      <li>
        <svg class="contact-icon" viewBox="0 0 16 16" aria-hidden="true"><path d="M1 5c0-2 3-3 7-3s7 1 7 3v1h-4V5H5v1H1z M3 8h10l1 6H2z"/></svg>
        209.555.0137
      </li>
      <li>
        <svg class="contact-icon" viewBox="0 0 16 16" aria-hidden="true"><path d="M4 1l3 3-2 2c1 2 3 4 5 5l2-2 3 3-2 3C7 15 1 9 1 3z"/></svg>
        209.555.0182
      </li>
      <li>
        <svg class="contact-icon" viewBox="0 0 16 16" aria-hidden="true"><path d="M4 0h8a1 1 0 0 1 1 1v14a1 1 0 0 1-1 1H4a1 1 0 0 1-1-1V1a1 1 0 0 1 1-1zm1 2v10h6V2zm3 11a1 1 0 1 0 0 2 1 1 0 0 0 0-2z"/></svg>
        209.555.0164
      </li>
      <li>
        <svg class="contact-icon" viewBox="0 0 16 16" aria-hidden="true"><path d="M1 3h14v10H1zm1 1v1l6 4 6-4V4zm0 3v5h12V7l-6 4z"/></svg>
        rtavener@hlit-example.com
      </li>
      <li>
        <svg class="contact-icon" viewBox="0 0 16 16" aria-hidden="true"><path d="M8 1a7 7 0 1 0 0 14A7 7 0 0 0 8 1zm0 1.2c.9.8 1.6 2.3 1.8 4.2H6.2C6.4 4.5 7.1 3 8 2.2zM5 6.4H2.4A5.8 5.8 0 0 1 6 2.5 8 8 0 0 0 5 6.4zm0 1.2a8 8 0 0 0 1 3.9 5.8 5.8 0 0 1-3.6-3.9zm1.2 0h3.6c-.2 1.9-.9 3.4-1.8 4.2-.9-.8-1.6-2.3-1.8-4.2zm4.8 0h2.6a5.8 5.8 0 0 1-3.6 3.9 8 8 0 0 0 1-3.9zm0-1.2a8 8 0 0 0-1-3.9 5.8 5.8 0 0 1 3.6 3.9z"/></svg>
        www.hlit-example.com
      </li>
    </ul>
    <div class="brand-block">
      <div class="brand-dot" aria-hidden="true"></div>
      <p class="brand-name">Harbor Lantern</p>
    </div>
  </section>

  <section class="card card-back" aria-label="Card back">
    <p class="brand-name">Harbor Lantern</p>
    <div class="brand-dot-large" aria-hidden="true"></div>
  </section>
</main>
</body>
</html>
```